Electrical flyer

We would like a flyer designed advertising "Does your house need a re-wire?" Potential fire hazards exist in houses constructed pre 1970. You're electrical cabling has insulation that corrodes leaving bare cables in the ceiling space. To find out more google VIR cable. To find out if you need a re-wire contact us on 0437 592 804 for a free assessment. We would like it to be quite confronting and grab peoples attention.

Target Market(s)

40-80 year olds

Industry/Entity Type

Electrical

Requirements
Must have
• Shock and confrontation, attention grabbing

```html
<!DOCTYPE html>
<html lang="en">
<head>
<meta charset="utf-8">
<title>Norvel Electrical – Re-wire Flyer</title>
<link rel="stylesheet" href="https://fonts.googleapis.com/css2?family=Oswald:wght@400;500;600;700&family=Lato:wght@400;700&display=swap">
<style>
  :root {
    --teal: #12979a;
    --teal-dark: #0e8184;
    --charcoal: #3b3e40;
    --ink: #2b2d2f;
    --paper: #ffffff;
    --stage: #e9eaec;
    --text: #3a3a3a;
  }
  * { box-sizing: border-box; margin: 0; padding: 0; }
  html, body { width: 1200px; height: 1200px; overflow: hidden; }
  body {
    background: var(--stage);
    display: flex; align-items: center; justify-content: center;
    font-family: "Lato", sans-serif;
  }
  .flyer {
    position: relative;
    width: 820px; height: 1160px;
    background: var(--paper);
    overflow: hidden;
    box-shadow: 0 4px 18px rgba(0,0,0,.18);
  }
  .hero-photo {
    position: absolute; left: 0; top: 0; width: 820px; height: 480px;
    background: radial-gradient(ellipse at 52% 52%, #f6b640 0%, #c9751c 22%, #6b3d17 50%, #2e231d 80%), #2e231d;
  }
  .hero-shapes { position: absolute; left: 0; top: 0; }
  .brand {
    position: absolute; left: 40px; top: 370px;
    width: 220px; text-align: center; color: #fff;
  }
  .brand-name {
    font-family: "Lato", sans-serif; font-weight: 700;
    font-size: 50px; line-height: 1; color: var(--teal);
    letter-spacing: 3px;
  }
  .brand-sub {
    font-size: 17px; letter-spacing: 7px; margin-top: 6px;
    border-top: 1px solid #fff; padding-top: 4px;
  }
  .brand-licence { font-size: 12px; letter-spacing: 8px; margin-top: 4px; }

  .headline {
    position: absolute; left: 40px; top: 520px; width: 480px;
    font-family: "Oswald", sans-serif; text-transform: uppercase;
  }
  .headline-main {
    display: block;
    font-weight: 600; font-size: 102px; line-height: .95;
    color: var(--teal); letter-spacing: -1px;
  }
  .headline-sub {
    display: block;
    font-weight: 600; font-size: 42px; line-height: 1.05;
    color: var(--ink); margin-top: 4px;
  }
  .hazard-badge { position: absolute; left: 560px; top: 530px; }

  .intro {
    position: absolute; left: 40px; top: 712px; width: 500px;
    font-size: 13px; line-height: 1.38; color: var(--text);
  }
  .services-title {
    position: absolute; left: 40px; top: 870px; width: 440px;
    font-family: "Oswald", sans-serif; font-weight: 500;
    font-size: 24px; line-height: 1.2; color: var(--teal);
  }
  .services {
    position: absolute; left: 40px; top: 938px;
    display: grid; grid-template-columns: 250px 230px; column-gap: 10px;
    font-size: 14px; color: var(--text);
  }
  .services ul { list-style: none; }
  .services li { margin-bottom: 6px; padding-left: 12px; position: relative; }
  .services li::before {
    content: ""; position: absolute; left: 0; top: 6px;
    width: 6px; height: 6px; border-radius: 50%; background: var(--teal);
  }
  .wires-photo {
    position: absolute; left: 560px; top: 790px; width: 260px; height: 344px;
    background: radial-gradient(ellipse at 65% 55%, #e7b23a 0%, #c9443b 30%, #3f86c2 55%, #f2f2f2 82%);
  }
  .cta {
    position: absolute; left: 40px; top: 1052px;
    padding-right: 22px; border-right: 1px solid #cfcfcf;
    font-family: "Oswald", sans-serif;
  }
  .cta-label { font-size: 24px; color: var(--teal); font-weight: 400; }
  .cta-phone { font-size: 36px; color: var(--ink); font-weight: 600; line-height: 1.1; }
  .contact {
    position: absolute; left: 300px; top: 1062px;
    list-style: none; font-size: 13px; color: var(--text);
  }
  .contact li { display: flex; align-items: center; gap: 8px; margin-bottom: 14px; }
  .footer-band {
    position: absolute; left: 0; bottom: 0; width: 820px; height: 26px;
    background: var(--charcoal);
  }
</style>
</head>
<body>
<main class="flyer">
  <div class="hero-photo" role="img" aria-label="Photo of two old light bulbs lying on sand against a glowing orange sunset sky"></div>
  <svg class="hero-shapes" width="820" height="500" viewBox="0 0 820 500">
    <polygon points="0,290 690,500 0,500" fill="#3b3e40"/>
    <polygon points="560,470 820,370 820,420 660,500 600,500" fill="#12979a"/>
    <polygon points="0,480 820,480 820,500 0,500" fill="#ffffff"/>
    <polygon points="0,480 650,480 690,500 0,500" fill="#3b3e40"/>
  </svg>

  <div class="brand">
    <div class="brand-name">NORVEL</div>
    <div class="brand-sub">ELECTRICAL</div>
    <div class="brand-licence">EC20387</div>
  </div>

  <h1 class="headline">
    <span class="headline-main">Does your</span>
    <span class="headline-sub">House need a re-wire?</span>
  </h1>

  <svg class="hazard-badge" width="230" height="230" viewBox="0 0 230 230" role="img" aria-label="Potential fire hazards exist in houses constructed pre 1970">
    <circle cx="115" cy="115" r="112" fill="#ffffff" stroke="#3b3e40" stroke-width="5"/>
    <circle cx="115" cy="115" r="98" fill="#12979a"/>
    <g fill="#ffffff" text-anchor="middle">
      <text x="115" y="90" font-family="Oswald, sans-serif" font-weight="600" font-size="28">Potential fire</text>
      <text x="115" y="112" font-family="Lato, sans-serif" font-size="14">hazards exist in houses</text>
      <text x="115" y="138" font-family="Oswald, sans-serif" font-weight="600" font-size="22">constructed pre</text>
      <text x="115" y="178" font-family="Oswald, sans-serif" font-weight="600" font-size="38">1970</text>
    </g>
  </svg>

  <p class="intro">The Norvel process is simple, easy and above board. Before starting a job, we listen to our customers so we know exactly what is required, and if there are any annoying long-term problems that need fixing for good while we're there. We discuss the optimal way to complete the work so that our customer is crystal clear on what will be done, when it will be done, what products will be used, and how much everything will cost. Then we set to work. Combining excellent craftsmanship with only the highest quality products, we ensure every Norvel customer walks away completely happy that the work they were quoted for is the work they received.</p>

  <h2 class="services-title">Norvel Electrical can take care of all your residential and commercial needs</h2>
  <div class="services">
    <ul>
      <li>Lighting installations</li>
      <li>Power installations</li>
      <li>Fault finding and maintenance</li>
      <li>Home renovations</li>
    </ul>
    <ul>
      <li>Telephone and data installs</li>
      <li>Antenna installs</li>
      <li>Testing and Tagging</li>
    </ul>
  </div>

  <div class="wires-photo" role="img" aria-label="Photo of coloured electrical cables coiled on a wiring plan"></div>

  <div class="cta">
    <div class="cta-label">for a free assessment</div>
    <div class="cta-phone">0437 592 804</div>
  </div>
  <ul class="contact">
    <li>
      <svg width="12" height="10" viewBox="0 0 12 10"><rect x="0.5" y="0.5" width="11" height="9" rx="1" fill="#12979a"/><polyline points="1,1 6,5.5 11,1" fill="none" stroke="#fff" stroke-width="1"/></svg>
      info@norvel.com.au
    </li>
    <li>
      <svg width="12" height="12" viewBox="0 0 12 12"><circle cx="6" cy="6" r="5.5" fill="#12979a"/><path d="M0.5 6h11M6 0.5c-2.5 3-2.5 8 0 11M6 0.5c2.5 3 2.5 8 0 11" fill="none" stroke="#fff" stroke-width=".8"/></svg>
      www.norvelelectrical.com.au
    </li>
  </ul>

  <div class="footer-band"></div>
</main>
</body>
</html>
```